Copper Ridge Business Cards For New Startup

I am looking for you to design some business cards for a new startup https://copperridgehub.example. I have supplied logo, brand guidelines and our signatures as a guide.

We need this to reflect the brand guidelines and the website for brand consistency,

What is Copper Ridge?

Mallorca's Business Growth Community
Join your new business community full of passionate entrepreneurs who
love to solve problems and help each other grow together!

Any questions you can ask.

Target Market(s)

Business to Business

Contact Information for Business Card

These are attached (signatures) to the job

Font styles to use
Other font styles liked:
• Open Sans

Requirements
Must have
• Match design guidelines
Nice to have
• Photos of our faces so people remember us

```html
<!DOCTYPE html>
<html lang="en">
<head>
<meta charset="utf-8">
<title>Copper Ridge Business Cards</title>
<link href="https://fonts.googleapis.com/css2?family=Open+Sans:wght@400;600;700&display=swap" rel="stylesheet">
<style>
  :root {
    --olive: #676b2d;
    --olive-dark: #4f5422;
    --olive-text: #6a6e2a;
    --bg-top: #959a72;
    --bg-bottom: #5b6130;
    --paper: #ffffff;
    --ink: #4a4a44;
    --photo-light: #eef0ee;
    --photo-mid: #c9d2dc;
    --photo-deep: #5f7596;
  }
  * { margin: 0; padding: 0; box-sizing: border-box; }
  html, body { width: 1200px; height: 895px; overflow: hidden; }
  body {
    background: linear-gradient(180deg, var(--bg-top) 0%, var(--bg-bottom) 100%);
    font-family: "Open Sans", Arial, sans-serif;
    position: relative;
  }
  .card {
    position: absolute;
    left: 290px;
    width: 620px;
    height: 354px;
    box-shadow: 0 6px 18px rgba(0,0,0,0.25);
    overflow: hidden;
  }
  .card-back { top: 62px; background: var(--olive); }
  .card-front { top: 458px; background: var(--paper); display: flex; }

  .brand {
    position: absolute;
    left: 40px;
    bottom: 40px;
    display: flex;
    align-items: center;
    gap: 16px;
  }
  .brand-circle {
    width: 52px; height: 52px;
    border: 2px solid var(--paper);
    border-radius: 50%;
  }
  .brand-name {
    color: var(--paper);
    font-weight: 600;
    font-size: 30px;
    letter-spacing: 1px;
    text-transform: uppercase;
  }

  .contact-panel {
    width: 262px;
    padding: 36px 0 0 30px;
    color: var(--ink);
    border-right: 3px solid var(--olive);
  }
  .person-name {
    color: var(--olive-text);
    font-size: 27px;
    line-height: 1.1;
    white-space: nowrap;
  }
  .person-name strong { font-weight: 700; }
  .person-role { font-size: 13px; margin-top: 6px; }
  .person-company { font-size: 13px; }
  .divider { width: 34px; height: 2px; background: var(--olive); margin: 12px 0 14px 40px; }
  .contact-list { list-style: none; font-size: 12px; line-height: 1.6; color: var(--olive-text); }
  .social-row { display: flex; gap: 9px; margin-top: 16px; }
  .social-row span {
    width: 26px; height: 26px;
    border: 1.5px solid var(--olive);
    border-radius: 50%;
  }
  .portrait {
    flex: 1;
    background:
      radial-gradient(ellipse at 55% 45%, #d8c2b0 0 12%, transparent 30%),
      linear-gradient(160deg, var(--photo-light) 0%, var(--photo-mid) 55%, var(--photo-deep) 100%);
  }
</style>
</head>
<body>
  <section class="card card-back">
    <div class="brand">
      <span class="brand-circle"></span>
      <span class="brand-name">Copper Ridge</span>
    </div>
  </section>

  <section class="card card-front">
    <div class="contact-panel">
      <h1 class="person-name"><strong>Daniel</strong> Marsh</h1>
      <p class="person-role">Founder &amp; Growth Hacker</p>
      <p class="person-company">Copper Ridge</p>
      <div class="divider"></div>
      <ul class="contact-list">
        <li>T: +44 7700 900 418</li>
        <li>E: dm@copperridgehub.example</li>
        <li>W: www.copperridgehub.example</li>
      </ul>
      <div class="social-row">
        <span></span><span></span><span></span><span></span><span></span>
      </div>
    </div>
    <div class="portrait" role="img" aria-label="Portrait photo of the founder in a blue blazer"></div>
  </section>
</body>
</html>
```